Website Design for Freeze-Dried Food Manufacturing Company (Pet Food & Agri-Food)

We are looking for a high-level web designer to create a clean, modern, premium website design for Brindle, a freeze-dried food manufacturing company operating in both the pet food and agri-food space.
This is not a basic website build β we are looking for a designer who understands brand positioning, layout, and user flow, not just visuals.
π― Project Objective
Design a website that:
Clearly communicates our capabilities and value proposition
Feels premium, credible, and product-driven
Guides users through a simple, intuitive journey
Clean and Crips
A critical requirement is clearly separating:
π Pet Food
π Agri-Food
These must feel like two distinct pathways within the same brand experience.
We have attached detailed documents outlining structure, layout, and messaging. These should be followed closely.
π What Success Looks Like
A high-impact homepage with strong visual hierarchy
Clear entry points into Pet Food and Agri-Food
Clean, intentional layout (not cluttered or template-like)
Thoughtful spacing, typography, and flow
A design that feels considered and elevated, not generic
π¨ Design Direction
We are aiming for a:
Minimal, premium aesthetic
Warm, natural color palette (creams, browns, muted tones)
Ingredient and product-focused visuals
Avoid:
Overly corporate / industrial styles
Generic SaaS-style layouts
Busy or over-designed interfaces
End Goal
A website that immediately communicates:
Who we are
What we do
Why weβre different
In a way that feels premium, clear, and easy to navigate.
Link to current website: https://brindleharvest.example/
https://brindlelabs.example/wp-admin/

```html
<!DOCTYPE html>
<html lang="en">
<head>
<meta charset="utf-8">
<title>Brindle — Industrial Freeze-Drying &amp; Food Manufacturing</title>
<link href="https://fonts.googleapis.com/css2?family=Figtree:wght@400;500;600;700&family=Inter:wght@400;500;600&display=swap" rel="stylesheet">
<style>
:root{
  --page:#f6f7f5;
  --ink:#1d2a22;
  --muted:#4a4f4b;
  --green:#52784a;
  --green-soft:#6c8f5f;
  --forest:#223d2a;
  --forest-2:#2c4a34;
  --pet:#e3e6de;
  --agri:#f3ece1;
  --cap-bg:#eceee8;
  --line:#d8dcd5;
  --white:#ffffff;
}
*{box-sizing:border-box;margin:0;padding:0}
html,body{width:1200px;height:4326px;overflow:hidden}
body{background:var(--page);font-family:"Inter",Arial,sans-serif;color:var(--ink);position:relative}
.abs{position:absolute}
h1,h2,h3,.display{font-family:"Figtree",Arial,sans-serif}
.btn{position:absolute;display:inline-flex;align-items:center;justify-content:center;height:30px;padding:0 22px;border-radius:16px;background:var(--green);color:#fff;font-size:10px;font-weight:600;text-decoration:none;font-family:"Inter",Arial,sans-serif}
.btn-ghost{background:transparent;border:1px solid rgba(255,255,255,.85)}
.center-x{left:50%;transform:translateX(-50%)}

/* header */
.site-header{position:absolute;top:0;left:0;width:1200px;height:62px;background:var(--white)}
.brand{position:absolute;font-family:"Figtree",Arial,sans-serif;font-weight:700;color:var(--forest);display:flex;align-items:center;gap:8px}
.brand .dot{width:12px;height:12px;border-radius:50%;background:var(--green)}
.site-header .brand{left:106px;top:12px;font-size:32px}
.main-nav{position:absolute;left:456px;top:24px;display:flex;gap:22px;font-size:10px;font-weight:500;color:var(--ink)}
.main-nav .active{color:var(--green)}
.site-header .btn{left:1000px;top:15px;height:32px;width:94px;padding:0}

/* hero */
.hero{position:absolute;top:62px;left:0;width:1200px;height:530px;background:linear-gradient(160deg,#6b7f4d 0%,#4e6a3a 35%,#3a5a2e 65%,#55703e 100%)}
.hero .shade{position:absolute;inset:0;background:linear-gradient(90deg,rgba(20,35,20,.55),rgba(20,35,20,.1) 65%)}
.hero .kicker{left:106px;top:140px;color:#fff;font-family:"Figtree",Arial,sans-serif;font-size:19px;font-weight:500}
.hero h1{left:106px;top:168px;color:#fff;font-size:40px;line-height:46px;font-weight:600;width:600px}
.hero p{left:106px;top:292px;color:#fff;font-size:11px;line-height:19px;width:440px}
.hero .btn{left:106px;top:362px;width:108px;padding:0}

/* pathway cards */
.pathway{position:absolute;top:617px;width:564px;height:407px}
.pathway.pet{left:25px;background:var(--pet)}
.pathway.agri{left:611px;background:var(--agri)}
.pathway .badge{position:absolute;left:-2px;top:-2px;width:60px;height:60px;border-radius:50%;background:#fff;display:flex;align-items:center;justify-content:center;box-shadow:0 2px 6px rgba(0,0,0,.06)}
.pathway h2{position:absolute;left:44px;top:112px;font-size:25px;font-weight:600}
.pathway .sub{position:absolute;left:44px;top:148px;font-size:11px;font-weight:600;color:var(--green)}
.pathway p{position:absolute;left:44px;top:180px;width:270px;font-size:13px;line-height:18px;color:var(--ink)}
.pathway .btn{left:44px;top:266px;width:120px;padding:0}
.pathway .visual{position:absolute;right:0;top:40px;width:250px;height:360px;border-radius:120px 0 0 0}
.pet .visual{background:linear-gradient(180deg,#d8a56c,#c99257 55%,#9a7252)}
.agri .visual{background:linear-gradient(160deg,#d9452f,#b8572a 45%,#5d8a3a 80%)}

.separation-note{position:absolute;left:25px;top:1050px;width:1150px;height:93px;background:linear-gradient(90deg,#f2e9df,#e4e8df);display:flex;align-items:center;justify-content:center;text-align:center;font-size:12px;font-weight:500;line-height:18px}

/* closed loop */
.section-title{position:absolute;left:0;width:1200px;text-align:center;font-size:28px;font-weight:500}
.section-lead{position:absolute;left:0;width:1200px;text-align:center;font-size:12px;color:var(--ink)}
.process{position:absolute;left:0;top:1327px;width:1200px;height:100px}
.step{position:absolute;width:120px;margin-left:-60px;text-align:center;font-size:12px;font-weight:500}
.step .ring{width:64px;height:64px;border-radius:50%;background:#eef0ea;margin:0 auto 14px;display:flex;align-items:center;justify-content:center}
.arrow{position:absolute;top:30px;width:40px;height:28px}

/* capabilities */
.capabilities{position:absolute;left:25px;top:1556px;width:1150px;height:441px;background:var(--cap-bg)}
.cap-card{position:absolute;top:1700px;width:182px;height:158px;background:#fff;text-align:center;padding-top:18px}
.cap-card h3{font-family:"Inter",Arial,sans-serif;font-size:11px;font-weight:600;margin-top:12px}
.cap-card p{font-size:8.5px;line-height:12px;color:var(--muted);margin:6px auto 0;width:160px}

/* why */
.why h2{position:absolute;left:200px;top:2102px;font-size:28px;font-weight:500}
.why-list{position:absolute;left:200px;top:2168px;width:371px;list-style:none}
.why-list li{height:62px;border-top:1px solid var(--line);display:flex;align-items:center;gap:14px;font-family:"Figtree",Arial,sans-serif;font-size:18px}
.why-list li:last-child{border-bottom:1px solid var(--line)}
.why-visual{position:absolute;left:612px;top:2071px;width:388px;height:438px;background:linear-gradient(135deg,#c78a55 0%,#b67545 40%,#cfc8bd 55%,#8d6a3c 75%,#b24a2a 100%)}

/* about */
.about{position:absolute;left:25px;top:2584px;width:1150px;height:406px;background:linear-gradient(135deg,#5a7a4d,#4a6b40 50%,#6a8558);overflow:hidden}
.about h2{position:absolute;left:175px;top:80px;color:#fff;font-size:28px;font-weight:500}
.about .tag{position:absolute;left:175px;top:142px;color:#fff;font-family:"Figtree",Arial,sans-serif;font-size:18px}
.about .intro{position:absolute;left:175px;top:184px;width:290px;color:#eef3ea;font-size:11.5px;line-height:18px}
.about .story{position:absolute;left:587px;top:80px;width:400px;color:#f2f5ef;font-size:11.5px;line-height:18px}
.about .story p{margin-bottom:18px}
.about .btn{left:587px;top:294px;width:110px;padding:0}
.about .watermark{position:absolute;left:80px;top:300px;font-family:"Figtree",Arial,sans-serif;font-size:118px;font-weight:700;color:rgba(255,255,255,.22);line-height:1}

/* food applications */
.tabs-line{position:absolute;left:200px;top:3164px;width:800px;height:1px;background:var(--line)}
.tabs{position:absolute;left:500px;top:3135px;display:flex;border:1px solid var(--forest)}
.tabs span{width:100px;height:30px;display:flex;align-items:center;justify-content:center;font-size:11px;font-weight:500;background:#fff}
.tabs .on{background:var(--forest);color:#fff}
.app-card{position:absolute;top:3265px;width:182px;height:187px;background:#fff}
.app-card .thumb{height:125px}
.app-card h3{font-family:"Inter",Arial,sans-serif;font-size:10px;font-weight:500;text-align:center;margin-top:16px;line-height:13px}

/* cta */
.footer-bg{position:absolute;left:0;top:3747px;width:1200px;height:579px;background:var(--forest)}
.cta{position:absolute;left:25px;top:3591px;width:1150px;height:324px;background:var(--green-soft)}
.cta h2{position:absolute;left:0;top:76px;width:1150px;text-align:center;color:#fff;font-size:28px;font-weight:500}
.cta p{position:absolute;left:0;top:128px;width:1150px;text-align:center;color:#eef3ea;font-size:17px;line-height:25px}
.cta .btn{left:522px;top:212px;width:106px;padding:0}

/* footer */
.site-footer .brand{left:106px;top:3984px;font-size:48px;color:#fff}
.site-footer .brand .dot{width:18px;height:18px;background:#8fb07f}
.foot-about{position:absolute;left:106px;top:4070px;width:250px;color:#dfe6dc;font-size:9px;line-height:19px}
.socials{position:absolute;left:106px;top:4163px;display:flex;gap:8px}
.socials span{width:30px;height:30px;border-radius:50%;border:1px solid rgba(255,255,255,.7)}
.foot-col h3{position:absolute;top:4010px;color:#fff;font-size:18px;font-weight:500}
.contact-list{position:absolute;left:420px;top:4056px;list-style:none;color:#e6ece3;font-size:9.5px}
.contact-list li{display:flex;gap:10px;margin-bottom:12px;line-height:14px}
.site-footer .dir{left:420px;top:4163px;width:104px;padding:0}
.quick-links{position:absolute;left:634px;top:4052px;list-style:none;color:#e6ece3;font-size:9.5px}
.quick-links li{height:21.3px}
.enquiry{position:absolute;left:794px;top:3960px;width:299px;height:366px;background:var(--forest-2);border:1px solid rgba(255,255,255,.15);border-bottom:none}
.enquiry h3{text-align:center;color:#fff;font-size:19px;font-weight:500;margin-top:28px}
.enquiry .hint{text-align:center;color:#e6ece3;font-size:10px;margin-top:6px}
.field{position:absolute;left:25px;width:249px;height:30px;background:#fff;border-radius:15px;font-size:9px;color:var(--ink);padding:0 14px;display:flex;align-items:center}
.field.area{height:56px;border-radius:14px;align-items:flex-start;padding-top:14px}
.enquiry .btn{left:100px;top:300px;width:98px;padding:0}
.foot-rule{position:absolute;left:106px;top:4250px;width:684px;height:1px;background:rgba(255,255,255,.2)}
.copyright{position:absolute;left:106px;top:4281px;color:#e6ece3;font-size:9px}
.copyright em{font-style:normal;color:#8fb07f}
.legal{position:absolute;left:420px;top:4281px;color:#e6ece3;font-size:9px;display:flex;gap:10px}
</style>
</head>
<body>

<header class="site-header">
  <div class="brand"><span>Brindle</span><span class="dot"></span></div>
  <nav class="main-nav">
    <span class="active">- Home -</span><span>About Us</span><span>Applications</span><span>Capabilities</span><span>Quality &amp; Traceability</span><span>Why Brindle</span><span>Contact</span>
  </nav>
  <a class="btn" href="#">Get Started</a>
</header>

<section class="hero" role="img" aria-label="Aerial photograph of the freeze-drying facility surrounded by green fields">
  <div class="shade"></div>
  <div class="abs kicker">Nutrition, Frozen in Time</div>
  <h1 class="abs">Industrial Freeze-Drying &amp; Food Manufacturing</h1>
  <p class="abs">A fully integrated, closed-loop system from ingredient sourcing through to production, packaging, and distribution</p>
  <a class="btn btn-ghost" href="#">Start a Project</a>
</section>

<article class="pathway pet">
  <div class="visual" role="img" aria-label="Photograph of a dog and a kitten beside a bowl of pet food"></div>
  <div class="badge"><svg width="26" height="26" viewBox="0 0 26 26" fill="var(--forest)"><circle cx="7" cy="9" r="2.6"/><circle cx="12" cy="6" r="2.6"/><circle cx="17" cy="9" r="2.6"/><ellipse cx="12" cy="16" rx="5" ry="4"/></svg></div>
  <h2>Pet Food</h2>
  <div class="sub">Applications &amp; Capabilities</div>
  <p>Freeze-dried meals, toppers, and treats designed for quality, consistency, and performance.</p>
  <a class="btn" href="#">Explore Pet Food</a>
</article>

<article class="pathway agri">
  <div class="visual" role="img" aria-label="Photograph of a crate of fresh vegetables"></div>
  <div class="badge"><svg width="26" height="26" viewBox="0 0 26 26" fill="none" stroke="var(--forest)" stroke-width="1.8"><path d="M6 20C6 10 12 6 20 6c0 8-4 14-14 14z"/><path d="M6 20l8-8"/></svg></div>
  <h2>Agri-Food</h2>
  <div class="sub">Applications &amp; Capabilities</div>
  <p>Ingredient processing and preservation solutions for food and agricultural applications.</p>
  <a class="btn" href="#">Explore Agri-Food</a>
</article>

<div class="separation-note">Pet food and agri-food production are handled in separate, controlled environments to ensure product<br>integrity and category-specific standards.</div>

<h2 class="section-title" style="top:1218px">A Complete, Closed-Loop System</h2>
<p class="section-lead" style="top:1276px">We manage every stage in-house, allowing full control over quality, consistency, and speed to market</p>

<div class="process">
  <div class="step" style="left:168px"><div class="ring"><svg width="30" height="30" viewBox="0 0 30 30" fill="none" stroke="var(--green)" stroke-width="1.4"><circle cx="15" cy="15" r="9"/><circle cx="15" cy="15" r="4"/><path d="M15 2v4M15 24v4M2 15h4M24 15h4"/></svg></div>Concept</div>
  <div class="step" style="left:310px"><div class="ring"><svg width="30" height="30" viewBox="0 0 30 30" fill="none" stroke="var(--green)" stroke-width="1.4"><path d="M5 24C5 12 13 6 25 6c0 12-8 18-20 18z"/><path d="M5 24l12-12"/></svg></div>Sourcing</div>
  <div class="step" style="left:455px"><div class="ring"><svg width="30" height="30" viewBox="0 0 30 30" fill="none" stroke="var(--green)" stroke-width="1.4"><circle cx="13" cy="13" r="8"/><path d="M19 19l7 7"/></svg></div>R&amp;D</div>
  <div class="step" style="left:597px"><div class="ring"><svg width="30" height="30" viewBox="0 0 30 30" fill="none" stroke="var(--green)" stroke-width="1.4"><path d="M15 3v24M4 9l22 12M26 9L4 21"/></svg></div>Freeze Drying</div>
  <div class="step" style="left:742px"><div class="ring"><svg width="30" height="30" viewBox="0 0 30 30" fill="none" stroke="var(--green)" stroke-width="1.4"><path d="M15 4l10 5v12l-10 5-10-5V9z"/><path d="M5 9l10 5 10-5M15 14v12"/></svg></div>Packaging</div>
  <div class="step" style="left:886px"><div class="ring"><svg width="30" height="30" viewBox="0 0 30 30" fill="none" stroke="var(--green)" stroke-width="1.4"><path d="M4 12l11-7 11 7v14H4z"/><rect x="10" y="16" width="10" height="10"/></svg></div>Storage</div>
  <div class="step" style="left:1029px"><div class="ring"><svg width="30" height="30" viewBox="0 0 30 30" fill="none" stroke="var(--green)" stroke-width="1.4"><path d="M15 3l11 6v12l-11 6-11-6V9z"/><circle cx="15" cy="15" r="4"/></svg></div>Distribution</div>
  <svg class="arrow" style="left:219px" viewBox="0 0 40 28" fill="none" stroke="#333" stroke-width="1"><path d="M2 6h34l-4-3M20 6v22"/></svg>
  <svg class="arrow" style="left:363px" viewBox="0 0 40 28" fill="none" stroke="#333" stroke-width="1"><path d="M2 6h34l-4-3M20 6v22"/></svg>
  <svg class="arrow" style="left:506px" viewBox="0 0 40 28" fill="none" stroke="#333" stroke-width="1"><path d="M2 6h34l-4-3M20 6v22"/></svg>
  <svg class="arrow" style="left:650px" viewBox="0 0 40 28" fill="none" stroke="#333" stroke-width="1"><path d="M2 6h34l-4-3M20 6v22"/></svg>
  <svg class="arrow" style="left:794px" viewBox="0 0 40 28" fill="none" stroke="#333" stroke-width="1"><path d="M2 6h34l-4-3M20 6v22"/></svg>
  <svg class="arrow" style="left:937px" viewBox="0 0 40 28" fill="none" stroke="#333" stroke-width="1"><path d="M2 6h34l-4-3M20 6v22"/></svg>
</div>
<a class="btn" href="#" style="left:545px;top:1450px;width:108px;padding:0">Start a Project</a>

<section class="capabilities"></section>
<h2 class="section-title" style="top:1632px">Our Capabilities</h2>
<div class="cap-card" style="left:200px"><svg width="34" height="40" viewBox="0 0 34 40" fill="none" stroke="var(--ink)" stroke-width="1.6"><path d="M8 8h18v28H8z"/><circle cx="17" cy="14" r="2"/><path d="M12 22h10v10H12z"/></svg><h3>OEM / Private Label</h3><p>Custom product development from concept to commercialization</p></div>
<div class="cap-card" style="left:406px"><svg width="40" height="40" viewBox="0 0 40 40" fill="none" stroke="var(--ink)" stroke-width="1.6"><path d="M20 4v32M6 12l28 16M34 12L6 28M16 6l4 4 4-4M16 34l4-4 4 4"/></svg><h3>Freeze Drying</h3><p>Industrial freeze-drying for food, ingredients, and agricultural products</p></div>
<div class="cap-card" style="left:612px"><svg width="40" height="40" viewBox="0 0 40 40" fill="none" stroke="var(--ink)" stroke-width="1.6"><path d="M10 22a6 6 0 0 1 2-11 8 8 0 0 1 16 0 6 6 0 0 1 2 11v12H10z"/><path d="M10 28h20"/></svg><h3>R&amp;D Test Kitchen</h3><p>Pilot runs, formulation, and product optimization</p></div>
<div class="cap-card" style="left:819px"><svg width="40" height="40" viewBox="0 0 40 40" fill="none" stroke="var(--ink)" stroke-width="1.6"><path d="M4 14L20 5l16 9v22H4z"/><path d="M11 20h18v16H11zM11 28h18M20 20v16"/></svg><h3>Storage &amp; Logistics</h3><p>We provide integrated storage solutions to support product stability and supply chain continuity.</p></div>
<a class="btn" href="#" style="left:545px;top:1890px;width:108px;padding:0">Start a Project</a>

<section class="why">
  <h2>Why Brindle</h2>
  <ul class="why-list">
    <li><svg width="24" height="20" viewBox="0 0 24 20" fill="none" stroke="var(--muted)" stroke-width="1.6"><rect x="2" y="5" width="13" height="13" transform="rotate(-10 8 11)"/><path d="M6 11l4 4L22 2"/></svg>Closed-loop manufacturing</li>
    <li><svg width="24" height="20" viewBox="0 0 24 20" fill="none" stroke="var(--muted)" stroke-width="1.6"><rect x="2" y="5" width="13" height="13" transform="rotate(-10 8 11)"/><path d="M6 11l4 4L22 2"/></svg>Integrated quality assurance</li>
    <li><svg width="24" height="20" viewBox="0 0 24 20" fill="none" stroke="var(--muted)" stroke-width="1.6"><rect x="2" y="5" width="13" height="13" transform="rotate(-10 8 11)"/><path d="M6 11l4 4L22 2"/></svg>Assurance full traceability</li>
    <li><svg width="24" height="20" viewBox="0 0 24 20" fill="none" stroke="var(--muted)" stroke-width="1.6"><rect x="2" y="5" width="13" height="13" transform="rotate(-10 8 11)"/><path d="M6 11l4 4L22 2"/></svg>Scalable production</li>
  </ul>
  <a class="btn" href="#" style="left:200px;top:2448px;width:108px;padding:0">Start a Project</a>
  <div class="why-visual" role="img" aria-label="Photograph of freeze-dried pet treats in bowls beside fresh vegetables"></div>
</section>

<section class="about" role="img" aria-label="Soft background photograph of freeze-dried food in a bowl with a green overlay">
  <h2>About Brindle</h2>
  <div class="tag">Nutrition, Frozen in Time</div>
  <p class="intro">Brindle was built out of a problem that became impossible to ignore.</p>
  <div class="story">
    <p>During COVID, we saw how much high-quality food was going to waste. farmers were left with surplus product and no efficient way to preserve or scale it.</p>
    <p>We saw an opportunity to change that...</p>
    <p>By leveraging freeze drying and building a fully integrated system around it, we created a way to transform perishable inputs into stable, high-quality products without compromising nutritional integrity.</p>
  </div>
  <a class="btn btn-ghost" href="#">Discover More</a>
  <div class="watermark">Brindle</div>
</section>

<h2 class="section-title" style="top:3066px">Food Applications</h2>
<div class="tabs-line"></div>
<div class="tabs"><span class="on">Pet Food</span><span>Agri Food</span></div>
<p class="section-lead" style="top:3196px;line-height:19px">We develop premium freeze-dried pet food products designed for performance,<br>palatability, and consistency.</p>
<div class="app-card" style="left:200px"><div class="thumb" role="img" aria-label="Photograph of balanced meals in green bowls with fresh ingredients" style="background:linear-gradient(135deg,#6fae4a,#b9905c 50%,#d66b4a)"></div><h3>K9 Veterinary Certified<br>Complete &amp; Balanced Meals</h3></div>
<div class="app-card" style="left:406px"><div class="thumb" role="img" aria-label="Photograph of freeze-dried pucks and cubes in a pink bowl" style="background:linear-gradient(135deg,#d9d4cc,#b7845a 50%,#e0457a)"></div><h3>Pucks and Cubes</h3></div>
<div class="app-card" style="left:612px"><div class="thumb" role="img" aria-label="Photograph of powders and toppers in bowls on a wooden table" style="background:linear-gradient(135deg,#8a5a3a,#d7c6b0 50%,#6b4a32)"></div><h3>Powders and Toppers</h3></div>
<div class="app-card" style="left:819px"><div class="thumb" role="img" aria-label="Photograph of a cat eating from a food bowl" style="background:linear-gradient(135deg,#e9a8b0,#c79a78 55%,#e2c9bf)"></div><h3>Custom Formats</h3></div>
<a class="btn" href="#" style="left:560px;top:3484px;width:80px;padding:0">View All</a>

<div class="footer-bg"></div>
<section class="cta" role="img" aria-label="Faint aerial photograph of farmland under a green overlay">
  <h2>Let’s Build Something Together</h2>
  <p>We work with agricultural and food partners to transform perishable inputs<br>into stable, value-added products</p>
  <a class="btn btn-ghost" href="#">Start a Project</a>
</section>

<footer class="site-footer">
  <div class="brand"><span>Brindle</span><span class="dot"></span></div>
  <p class="foot-about">A fully integrated, closed-loop system from ingredient sourcing through to production, packaging, and distribution</p>
  <div class="socials"><span></span><span></span><span></span><span></span></div>

  <div class="foot-col"><h3 style="left:420px">Contact us</h3></div>
  <ul class="contact-list">
    <li><svg width="12" height="12" viewBox="0 0 12 12" fill="none" stroke="#fff" stroke-width="1"><path d="M2 1h2l1 3-1.5 1a6 6 0 0 0 3 3L8 6.5l3 1v2a1 1 0 0 1-1 1A9 9 0 0 1 1 2a1 1 0 0 1 1-1z"/></svg>+1-555-014-2290</li>
    <li><svg width="12" height="12" viewBox="0 0 12 12" fill="none" stroke="#fff" stroke-width="1"><rect x="1" y="2.5" width="10" height="7"/><path d="M1 3l5 4 5-4"/></svg>hello@brindleharvest.example</li>
    <li><svg width="12" height="12" viewBox="0 0 12 12" fill="none" stroke="#fff" stroke-width="1"><path d="M6 11S2 7 2 4.5a4 4 0 0 1 8 0C10 7 6 11 6 11z"/><circle cx="6" cy="4.5" r="1.3"/></svg><span>42 Orchard Lane, Fernhill, ON.<br>F-1180</span></li>
  </ul>
  <a class="btn dir" href="#">Get Direction</a>

  <div class="foot-col"><h3 style="left:634px">Quick links</h3></div>
  <ul class="quick-links">
    <li>Home</li><li>About Us</li><li>Applications</li><li>Capabilities</li><li>Quality &amp; Traceability</li><li>Why Brindle</li><li>Contact</li>
  </ul>

  <div class="enquiry">
    <h3>Start a Projects</h3>
    <p class="hint">Fill in the form below and we’ll call you.</p>
    <div class="field" style="top:109px">Name</div>
    <div class="field" style="top:153px">Phone</div>
    <div class="field" style="top:196px">Email</div>
    <div class="field area" style="top:225px">How can we help you?</div>
    <a class="btn" href="#">Get Started</a>
  </div>

  <div class="foot-rule"></div>
  <p class="copyright">© 2026 <em>Brindle</em>. All rights reserved.</p>
  <p class="legal"><span>Privacy policy</span><span>|</span><span>Terms and conditions</span></p>
</footer>

</body>
</html>
```